218mugs - order 500,000 info graphic

At 218mugs we celebrate the milestones for our orders, for 10k we did a t-shirt and for 150k we did a biscuit, for 365k we gave away 218mugs of coffee and we are about to hit 500,000 orders.

We are after an infographic to illustrate our numbers, stats and facts. We want in to be inline with the 218mugs look and feel and we want it to be clear yet highly engaging (ie sharable web social and pdf) We want the info graphic to reflect us and our business and deliver the numbers. As this is a time sensitve project we would like the graphic ready to go and just make final adjustments to numbers once we reach the milestone.

Please check out our website and social media and ask any questions

Target Market(s)

this will go out with our media release, and will be used as a marketing tool

Font styles to use
Sans Serif

Colors
f37022
acd036
cadf82

Requirements
Must have
• if the design is right, we want to take elements and use in other mediums ... tshirts/stickers
Nice to have
• I want it nice and clean, I know I have a lot of info but I wont it to be clean and flow ... the hero is the 500,000 orders
Should not have
• we aren't an App company, we want to be seen as a global tech complany and 218mugs is product of that

```html
<!DOCTYPE html>
<html lang="en">
<head>
<meta charset="utf-8">
<title>218mugs – 500,000 Cups Infographic</title>
<link href="https://fonts.googleapis.com/css2?family=Bebas+Neue&family=Lora:ital@0;1&family=Open+Sans:wght@400;600&display=swap" rel="stylesheet">
<style>
  :root {
    --orange: #f37022;
    --green: #acd036;
    --green-light: #cadf82;
    --ink: #231f20;
    --cream: #fdf3c9;
    --cream-edge: #fad596;
    --white: #ffffff;
    --brown: #7a2412;
    --brown-light: #a8442a;
  }
  * { box-sizing: border-box; margin: 0; padding: 0; }
  html, body { width: 757px; height: 1200px; overflow: hidden; }
  body { font-family: "Bebas Neue", "Arial Narrow", sans-serif; color: var(--ink); }

  .infographic {
    position: relative; width: 757px; height: 1200px; overflow: hidden;
    background: radial-gradient(ellipse at 50% 45%, var(--cream) 0%, #fce9b3 60%, var(--cream-edge) 100%);
  }
  .abs { position: absolute; line-height: 1; white-space: nowrap; }

  /* header */
  .header-band { position: absolute; left: 0; top: 0; width: 757px; height: 94px; background: var(--green); }
  .header-title { left: 0; width: 757px; text-align: center; top: 12px; font-size: 62px; color: var(--white); letter-spacing: 1px; }
  .header-sub { right: 28px; top: 70px; font-family: "Lora", serif; font-size: 20px; color: var(--white); }
  .awning { position: absolute; left: 0; top: 100px; }

  /* popular order */
  .intro-line { left: 25px; top: 172px; font-size: 44px; }
  .hero-drink { left: 23px; top: 214px; font-size: 96px; color: var(--orange); }
  .orders-line { left: 25px; top: 305px; font-size: 50px; }
  .orders-line .accent, .worth-line .accent { color: var(--orange); }
  .worth-line { left: 25px; top: 360px; font-size: 28px; }
  .cup-illustration {
    position: absolute; left: 540px; top: 176px; width: 195px; height: 205px;
    background: radial-gradient(circle at 45% 70%, var(--brown-light) 0%, var(--brown) 65%, rgba(122,36,18,0) 72%);
  }

  .divider { position: absolute; left: 0; width: 757px; border-top: 2px dashed var(--orange); }
  .divider-v { position: absolute; border-left: 2px dashed var(--orange); }

  /* extras */
  .but { left: 23px; top: 428px; font-size: 84px; color: var(--orange); }
  .not-just { left: 108px; top: 430px; font-size: 25px; }
  .coffee-word { left: 106px; top: 452px; font-size: 56px; }
  .extras-q { left: 25px; top: 520px; font-size: 26px; }
  .extras-icons { position: absolute; left: 25px; top: 560px; width: 258px; height: 70px; }
  .icon { position: absolute; top: 0; height: 70px; background: var(--orange); border-radius: 6px; }
  .extras-a { left: 25px; top: 640px; font-size: 29px; }

  .chart-title { left: 305px; top: 428px; font-size: 46px; }
  .chart-note { right: 23px; top: 476px; font-size: 21px; color: var(--orange); }
  .chart { position: absolute; left: 300px; top: 480px; }

  /* stats */
  .stats { position: absolute; left: 22px; top: 692px; width: 715px; height: 70px; display: flex; align-items: center; justify-content: space-between; }
  .stat { display: flex; align-items: center; gap: 8px; }
  .stat-value { font-size: 66px; color: var(--green); line-height: 1; }
  .stat-label { font-size: 26px; line-height: 0.92; }

  /* demand */
  .demand-chart { position: absolute; left: 0; top: 780px; }
  .bubble {
    position: absolute; background: var(--white); border-radius: 6px; padding: 7px 10px;
    font-family: "Open Sans", sans-serif; font-size: 11px; color: var(--ink);
    box-shadow: 0 2px 4px rgba(0,0,0,0.25); white-space: nowrap;
  }
  .bubble::after { content: ""; position: absolute; border: 8px solid transparent; }
  .bubble-one { left: 58px; top: 810px; }
  .bubble-one::after { right: 30px; bottom: -15px; border-top-color: var(--white); }
  .bubble-two { left: 204px; top: 890px; }
  .bubble-two::after { left: 10px; top: -15px; border-bottom-color: var(--white); }
  .per-day-num { left: 382px; top: 880px; font-size: 48px; }
  .per-day-label { left: 496px; top: 878px; font-size: 25px; line-height: 0.92; }
  .evolve { left: 52px; top: 937px; font-size: 28px; color: var(--green); }
  .support-num { left: 588px; top: 792px; font-size: 100px; color: var(--orange); }
  .support-word { left: 582px; top: 876px; font-size: 66px; }
  .support-by { left: 588px; top: 934px; font-size: 32px; }

  /* call to action */
  .cta-1 { left: 23px; top: 1004px; font-size: 62px; color: var(--orange); }
  .cta-2 { left: 23px; top: 1064px; font-size: 56px; }
  .cta-now { left: 424px; top: 1002px; font-size: 142px; color: var(--green); }
  .cta-platforms { left: 606px; top: 1008px; width: 136px; text-align: center; font-size: 29px; line-height: 1.02; white-space: normal; }

  .footer-band { position: absolute; left: 0; top: 1128px; width: 757px; height: 72px; background: var(--green); }
  .footer-text { left: 0; width: 757px; text-align: center; top: 1149px; font-size: 38px; color: var(--white); letter-spacing: 1px; }
</style>
</head>
<body>
<main class="infographic">

  <header>
    <div class="header-band"></div>
    <h1 class="abs header-title">WE'VE REACHED 500,000 CUPS!</h1>
    <p class="abs header-sub">Now that's a lot of coffee!</p>
    <svg class="awning" width="757" height="46" viewBox="0 0 757 46">
      <rect x="0" y="0" width="757" height="16" fill="var(--orange)"/>
      <g fill="var(--orange)">
        <circle cx="0" cy="16" r="29"/><circle cx="63" cy="16" r="29"/><circle cx="126" cy="16" r="29"/>
        <circle cx="189" cy="16" r="29"/><circle cx="252" cy="16" r="29"/><circle cx="315" cy="16" r="29"/>
        <circle cx="378" cy="16" r="29"/><circle cx="441" cy="16" r="29"/><circle cx="504" cy="16" r="29"/>
        <circle cx="567" cy="16" r="29"/><circle cx="630" cy="16" r="29"/><circle cx="693" cy="16" r="29"/>
        <circle cx="756" cy="16" r="29"/>
      </g>
      <rect x="0" y="-20" width="757" height="20" fill="var(--green)"/>
    </svg>
  </header>

  <section class="popular">
    <p class="abs intro-line">AND THE MOST POPULAR ORDER IS...</p>
    <h2 class="abs hero-drink">THE CAPPUCCINO</h2>
    <p class="abs orders-line">WITH <span class="accent">199,815</span> ORDERS PLACED</p>
    <p class="abs worth-line">THAT'S <span class="accent">$816,662</span> WORTH OF THE ITALIAN FAVOURITE</p>
    <div class="cup-illustration" role="img" aria-label="Steaming cup of coffee with a number one ribbon badge"></div>
  </section>

  <div class="divider" style="top:408px"></div>
  <div class="divider-v" style="left:293px; top:416px; height:252px"></div>

  <section class="extras">
    <p class="abs but">BUT</p>
    <p class="abs not-just">WE DON'T JUST DO</p>
    <p class="abs coffee-word">COFFEE</p>
    <p class="abs extras-q">FOOD? DRINK? NEWSPAPER?</p>
    <div class="extras-icons">
      <div class="icon" style="left:0; width:100px; border-radius:40px 40px 10px 10px" role="img" aria-label="Burger icon"></div>
      <div class="icon" style="left:112px; width:44px" role="img" aria-label="Drink cup icon"></div>
      <div class="icon" style="left:168px; width:88px" role="img" aria-label="Newspaper icon"></div>
    </div>
    <p class="abs extras-a">YEP, ANYTHING YOU NEED!</p>
  </section>

  <section class="sales">
    <h2 class="abs chart-title">SO WHAT ELSE DO YOU LIKE?</h2>
    <p class="abs chart-note">500,000 CUPS SOLD!</p>
    <svg class="chart" width="450" height="190" viewBox="300 480 450 190" font-family="Bebas Neue, sans-serif">
      <g stroke="var(--orange)" stroke-width="1">
        <line x1="347" y1="493" x2="742" y2="493"/>
        <line x1="347" y1="535" x2="742" y2="535"/>
        <line x1="347" y1="578" x2="742" y2="578"/>
        <line x1="347" y1="620" x2="742" y2="620"/>
      </g>
      <g font-size="8" fill="var(--ink)">
        <text x="335" y="495">200</text><text x="335" y="537">150</text>
        <text x="335" y="580">100</text><text x="338" y="622">50</text>
      </g>
      <text transform="translate(325 663) rotate(-90)" font-size="18" fill="var(--green)">AMOUNT SOLD X1000</text>
      <g fill="var(--green)">
        <rect x="352" y="503" width="56" height="160"/>
        <rect x="417" y="535" width="57" height="128"/>
        <rect x="482" y="551" width="56" height="112"/>
        <rect x="548" y="637" width="57" height="26"/>
        <rect x="614" y="650" width="56" height="13"/>
        <rect x="679" y="614" width="56" height="49"/>
      </g>
      <g fill="var(--green-light)">
        <rect x="380" y="503" width="28" height="160"/>
        <rect x="446" y="535" width="28" height="128"/>
        <rect x="510" y="551" width="28" height="112"/>
        <rect x="577" y="637" width="28" height="26"/>
        <rect x="642" y="650" width="28" height="13"/>
        <rect x="707" y="614" width="28" height="49"/>
      </g>
      <line x1="347" y1="663" x2="742" y2="663" stroke="var(--green)" stroke-width="2"/>
      <g font-size="11" fill="var(--white)">
        <text x="354" y="513">CAPPUCCINO</text>
        <text x="419" y="545">CAFFE LATTE</text>
        <text x="484" y="561">FLAT WHITE</text>
        <text x="550" y="647">MOCHACCINO</text>
        <text x="615" y="659">HOT CHOCOLATE</text>
        <text x="681" y="624">THE OTHERS</text>
      </g>
    </svg>
  </section>

  <div class="divider" style="top:675px"></div>

  <section class="stats">
    <div class="stat"><span class="stat-value">500,000</span><span class="stat-label">TOTAL<br>ORDERS</span></div>
    <div class="stat"><span class="stat-value">$3.5M</span><span class="stat-label">TOTAL<br>VALUE</span></div>
    <div class="stat"><span class="stat-value">$7.11</span><span class="stat-label">AVERAGE PRICE<br>PER ORDER</span></div>
  </section>

  <div class="divider" style="top:775px"></div>
  <div class="divider-v" style="left:565px; top:782px; height:196px"></div>

  <section class="demand">
    <svg class="demand-chart" width="560" height="190" viewBox="0 780 560 190" font-family="Bebas Neue, sans-serif">
      <text transform="translate(38 955) rotate(-90)" font-size="20" fill="var(--green)">CONSUMER DEMAND</text>
      <polyline points="57,920 185,851 268,835 319,879 408,828 459,856 522,810"
        fill="none" stroke="var(--green)" stroke-width="8" stroke-linejoin="miter"/>
      <polygon points="512,796 548,798 530,828" fill="var(--green)"/>
    </svg>
    <p class="bubble bubble-one">"White with one please"</p>
    <p class="bubble bubble-two">"I'll have a Mocha thanks!"</p>
    <p class="abs per-day-num">1,562</p>
    <p class="abs per-day-label">ORDERS<br>PER DAY</p>
    <p class="abs evolve">AND WE CONTINUE TO EVOLVE WITH CUSTOMER DEMAND</p>
  </section>

  <section class="support">
    <p class="abs support-num">24/7</p>
    <p class="abs support-word">SUPPORT</p>
    <p class="abs support-by">BY REAL PEOPLE</p>
  </section>

  <div class="divider" style="top:984px"></div>

  <section class="cta">
    <p class="abs cta-1">GET YOUR FREE APP</p>
    <p class="abs cta-2">IT'S EASY TO DOWNLOAD</p>
    <p class="abs cta-now">NOW</p>
    <p class="abs cta-platforms">AVAILABLE FOR FONIX AND DROIDEX</p>
  </section>

  <footer>
    <div class="footer-band"></div>
    <p class="abs footer-text">WE ARE 218MUGS.COM</p>
  </footer>

</main>
</body>
</html>
```